It must be unique & Proffessional
VORNA GROUP
# 130 Very nice, could you please use the “symbols” for Phone, cellphone and so on, instead of writing “p:” and “c:”. You did that by # 69 :-)
Thanks for all your very creative suggestions.
A general comment:
- Please correct the “projektchef” to “Direktør”
- Please add at fixed telephone number +45 62 18 37 51
- Please add “+45” in front of the cellphone number
- Please make the envelope as window envelops, and logo bottom right corner
- On the A4 paper, we need the logo in top right corner
#61,Very good design, please make the backside as you’ve done by #64
#128Please leave the bottom of the paper free of text and colors, and add only one thin line 13 mm from the page bottom.
Again very good designs, thank you very much
Logo AI file is now uploaded :-)
Now we have our Logo ready, looking forward to see your suggestions for design :-)
TK/RWF Team
Logo is currently being designed, you can participate if you would like to :-)

```html
<!DOCTYPE html>
<html lang="da">
<head>
<meta charset="utf-8">
<title>VORNA GROUP – Visitkort</title>
<link rel="stylesheet" href="https://fonts.googleapis.com/css2?family=Roboto:wght@400;700;900&display=swap">
<style>
  :root {
    --backdrop: #e9e7e4;
    --card: #ffffff;
    --brand-red: #b3181d;
    --brand-red-dark: #8e1014;
    --brand-grey: #4a4a4a;
    --text-light: #ffffff;
  }
  * { margin: 0; padding: 0; box-sizing: border-box; }
  html, body {
    width: 1200px; height: 530px; overflow: hidden;
    background: var(--backdrop);
    font-family: "Roboto", Arial, sans-serif;
  }
  .sheet { position: relative; width: 1200px; height: 530px; }
  .card {
    position: absolute; top: 100px;
    width: 552px; height: 332px;
    background: var(--card);
    border-radius: 16px;
    overflow: hidden;
    box-shadow: 0 6px 14px rgba(0,0,0,.18);
  }
  .card--front { left: 24px; }
  .card--back { left: 624px; }

  .brand {
    position: absolute; left: 0; right: 0;
    display: flex; align-items: center; justify-content: center; gap: 14px;
  }
  .brand__square { width: 26px; height: 26px; background: var(--brand-grey); }
  .brand__name {
    font-weight: 900; font-size: 44px; letter-spacing: 1px;
    color: var(--brand-red);
  }
  .card--front .brand { top: 72px; }
  .card--back .brand { top: 118px; }

  .contact-band {
    position: absolute; left: 0; right: 0; bottom: 0; height: 122px;
    background: linear-gradient(180deg, var(--brand-red), var(--brand-red-dark));
    color: var(--text-light);
    text-align: center;
  }
  .contact-band__notch { position: absolute; top: -1px; left: 50%; margin-left: -16px; }
  .contact-band__name {
    margin-top: 18px; font-size: 17px; font-weight: 700; letter-spacing: .3px;
  }
  .contact-band__role { font-weight: 400; font-size: 14px; margin-left: 4px; }
  .contact-band__address { margin-top: 6px; font-size: 14px; }
  .contact-band__lines {
    margin-top: 6px; font-size: 13px;
    display: flex; justify-content: center; gap: 22px;
  }
  .contact-item { display: inline-flex; align-items: center; gap: 6px; }
  .contact-item svg { width: 13px; height: 13px; flex: none; }
</style>
</head>
<body>
<main class="sheet">
  <section class="card card--front">
    <div class="brand">
      <span class="brand__square"></span>
      <span class="brand__name">VORNA GROUP</span>
    </div>
    <div class="contact-band">
      <svg class="contact-band__notch" width="32" height="14" viewBox="0 0 32 14" aria-hidden="true">
        <polygon points="0,0 32,0 16,14" fill="#ffffff"/>
      </svg>
      <p class="contact-band__name">KASPER HOLMVIG<span class="contact-band__role">Direktør</span></p>
      <p class="contact-band__address">Rønnebærvej 9, 7100 Vejle, Denmark</p>
      <div class="contact-band__lines">
        <span class="contact-item">
          <svg viewBox="0 0 16 16" aria-label="Telefon"><path fill="#fff" d="M3.5 1.5l2.5 0 1 3.5-1.6 1.2c.8 1.7 2.2 3.1 3.9 3.9L10.5 8.5l3.5 1v2.5c0 .8-.7 1.5-1.5 1.5C7 13.5 2 8.5 2 3c0-.8.7-1.5 1.5-1.5z"/></svg>
          +45 62 18 37 51
        </span>
        <span class="contact-item">
          <svg viewBox="0 0 16 16" aria-label="Mobil"><rect x="4" y="1" width="8" height="14" rx="1.5" fill="#fff"/><rect x="5.3" y="2.8" width="5.4" height="8.6" fill="#a01418"/><circle cx="8" cy="13.1" r=".8" fill="#a01418"/></svg>
          +45 41 73 29 06
        </span>
      </div>
      <div class="contact-band__lines">
        <span class="contact-item">
          <svg viewBox="0 0 16 16" aria-label="E-mail"><rect x="1" y="3" width="14" height="10" rx="1" fill="#fff"/><path d="M1.5 3.8L8 9l6.5-5.2" fill="none" stroke="#a01418" stroke-width="1.3"/></svg>
          kh@vornagroup.com
        </span>
        <span class="contact-item">
          <svg viewBox="0 0 16 16" aria-label="Web"><circle cx="8" cy="8" r="6.3" fill="none" stroke="#fff" stroke-width="1.4"/><ellipse cx="8" cy="8" rx="2.6" ry="6.3" fill="none" stroke="#fff" stroke-width="1.2"/><path d="M1.8 8h12.4" stroke="#fff" stroke-width="1.2"/></svg>
          www.vornagroup.com
        </span>
      </div>
    </div>
  </section>

  <section class="card card--back">
    <div class="brand">
      <span class="brand__square"></span>
      <span class="brand__name">VORNA GROUP</span>
    </div>
    <p class="web" style="position:absolute;left:0;right:0;top:212px;text-align:center;font-size:15px;font-weight:700;letter-spacing:1px;color:var(--brand-red);">www.vornagroup.com</p>
  </section>
</main>
</body>
</html>
```